Business card design needed

Want the logo on a medium blue background and a nice funky design. I have my own gym and run one on one personal training and nutrition sessions. want it to look lively.
Updates

Please note I requested my logo on a blue background 

PLEASE NOTE: I already have a logo. It is attached to the order!!

Target Market(s)

over 55s

Industry/Entity Type

Nutrition

Contact Information for Business Card

Front of card : Logo ( on blue background )
Keldra Ashby
Nutrition & Fitness Coach for Seniors
Private gym at : 17 Tindal Crescent, Wembury, Perth, WA 6166
Mob : 0418372651
Email : keldraashby@frelmo.com
"For Seniors by a Senior"

Back of card
B.A. ( Soc.)
Dip. Ed. (Sec.)
Wellness Coach
Cert 4 Personal Trainer
Cert. Nutritition
MOVE ON Facilitator
Ageing Boldly Moving Freely Facilitator
NLP Master

```html
<!DOCTYPE html>
<html lang="en">
<head>
<meta charset="utf-8">
<title>Silver Stride Nutrition &amp; Fitness – Business Card</title>
<link rel="stylesheet" href="https://fonts.googleapis.com/css2?family=Source+Sans+3:wght@400;600;700&display=swap">
<style>
  :root {
    --stage: #1c1c1c;
    --card: #0a3a5a;
    --arc: #0d4d78;
    --accent-blue: #0f64a0;
    --brand-yellow: #f0e43a;
    --text-light: #e6ebef;
    --text-muted: #d3dbe2;
  }
  * { margin: 0; padding: 0; box-sizing: border-box; }
  html, body {
    width: 1200px; height: 900px; overflow: hidden;
    background: var(--stage);
    font-family: "Source Sans 3", Arial, sans-serif;
  }
  .canvas { position: relative; width: 1200px; height: 900px; }
  .card {
    position: absolute; width: 596px; height: 330px;
    background: var(--card); overflow: hidden;
    color: var(--text-light);
    box-shadow: 2px 3px 4px rgba(0,0,0,0.45);
  }
  .card--front { left: 126px; top: 92px; }
  .card--back { left: 469px; top: 470px; }
  .card__arc { position: absolute; inset: 0; }
  .brand {
    position: absolute; left: 112px; top: 26px;
    display: flex; align-items: center; gap: 12px;
  }
  .brand__dot { width: 20px; height: 20px; border-radius: 50%; background: var(--brand-yellow); }
  .brand__name {
    color: var(--brand-yellow); font-weight: 600; font-size: 22px; line-height: 1.3;
  }
  .person { position: absolute; left: 30px; top: 166px; }
  .person__name { font-size: 28px; font-weight: 700; letter-spacing: 0.4px; line-height: 1.1; }
  .person__role { font-size: 11.5px; margin-left: 90px; margin-top: 0; color: var(--text-muted); }
  .tagline { position: absolute; left: 30px; top: 285px; font-size: 12px; }
  .contact { position: absolute; left: 320px; top: 242px; list-style: none; }
  .contact__item { display: flex; align-items: center; gap: 8px; font-size: 12px; height: 21px; }
  .contact__item--phone { font-size: 14px; }
  .contact__icon { width: 12px; height: 12px; fill: var(--text-light); flex: none; }
  .back-decoration {
    position: absolute; left: 140px; top: 0; width: 456px; height: 330px;
    background: radial-gradient(ellipse 70% 60% at 62% 45%, rgba(15,100,160,0.75), rgba(15,100,160,0.25) 60%, rgba(10,58,90,0) 100%);
  }
  .credentials { position: absolute; left: 50px; top: 86px; list-style: none; z-index: 1; }
  .credentials__item { font-size: 12px; height: 21.2px; color: var(--text-light); }
  .credentials__item::before { content: "• "; }
</style>
</head>
<body>
<main class="canvas">
  <section class="card card--front" aria-label="Card front">
    <svg class="card__arc" viewBox="0 0 596 330" aria-hidden="true">
      <path d="M496 0 C 420 95, 240 160, 0 110 L0 116 C 245 168, 428 100, 506 0 Z" fill="var(--arc)"/>
    </svg>
    <div class="brand">
      <span class="brand__dot"></span>
      <span class="brand__name">Silver Stride<br>Nutrition &amp; Fitness</span>
    </div>
    <div class="person">
      <h1 class="person__name">Keldra Ashby</h1>
      <p class="person__role">Nutrition &amp; Fitness Coach</p>
    </div>
    <p class="tagline">“For Seniors by a Senior”</p>
    <ul class="contact">
      <li class="contact__item contact__item--phone">
        <svg class="contact__icon" viewBox="0 0 24 24"><path d="M6.6 10.8a15 15 0 0 0 6.6 6.6l2.2-2.2c.3-.3.7-.4 1-.2 1.1.4 2.3.6 3.6.6.6 0 1 .4 1 1V20c0 .6-.4 1-1 1A17 17 0 0 1 3 4c0-.6.4-1 1-1h3.5c.6 0 1 .4 1 1 0 1.3.2 2.5.6 3.6.1.3 0 .7-.2 1z"/></svg>
        0418-372-651
      </li>
      <li class="contact__item">
        <svg class="contact__icon" viewBox="0 0 24 24"><path d="M2 5h20v14H2z M3.5 6.5 12 13l8.5-6.5" fill="none" stroke="var(--text-light)" stroke-width="2"/></svg>
        keldraashby@frelmo.com
      </li>
      <li class="contact__item">
        <svg class="contact__icon" viewBox="0 0 24 24"><path d="M12 2a7 7 0 0 0-7 7c0 5 7 13 7 13s7-8 7-13a7 7 0 0 0-7-7zm0 9.5a2.5 2.5 0 1 1 0-5 2.5 2.5 0 0 1 0 5z"/></svg>
        17 Tindal Crescent, Wembury, Perth, WA 6166
      </li>
    </ul>
  </section>

  <section class="card card--back" aria-label="Card back">
    <div class="back-decoration" role="img" aria-label="Large brand decoration in bright blue"></div>
    <ul class="credentials">
      <li class="credentials__item">B.A.</li>
      <li class="credentials__item">Dip. Ed.</li>
      <li class="credentials__item">Wellness Coach</li>
      <li class="credentials__item">Cert 4 Personal Trainer</li>
      <li class="credentials__item">Cert Nutrition</li>
      <li class="credentials__item">MOVE ON Facilitator</li>
      <li class="credentials__item">Ageing Boldly Moving Freely Facilitator</li>
      <li class="credentials__item">NLP Master</li>
    </ul>
  </section>
</main>
</body>
</html>
```